azure haven of northeast florida business card

I need a new attractive business card. I am planning on printing on very thick rounded corner stock and having painted edges. We are a swimming pool remodel, repair, and service company in north florida. Our current logo is red, white, and blue. It doesn't necessarily have to stay that way, I am open to other ideas. It will need to contain my name, work and cell numbers, email, website, and my contractor license number.

Target Market(s)

High end residential and commercial clients

Industry/Entity Type

Business

Contact Information for Business Card

Company name, employee name and title, work and cell phone numbers, email and website, and Contractor number.

our work scope should be on card somewhere: remodel ~ repair ~ service

logo or slight variation of logo also. (not necessarily set on keeping exact logo)

Colors

Designer to choose colors to be used in the design.

Requirements
Nice to have
• We deal with water so I think some sort of water element or just a color similar to pool water would be nice to integrate into design.

```html
<!DOCTYPE html>
<html lang="en">
<head>
<meta charset="utf-8">
<title>Azure Haven of Northeast Florida – Business Card</title>
<link rel="stylesheet" href="https://fonts.googleapis.com/css2?family=Cinzel:wght@700&family=Open+Sans:wght@400;600;700&display=swap">
<style>
  :root {
    --stage: #1c1c1e;
    --navy: #040833;
    --accent-blue: #1e7fd0;
    --text-light: #c9d3e6;
    --white: #ffffff;
    --water-deep: #0d3f8f;
    --water-mid: #1d67c2;
    --water-light: #5fa4e6;
  }
  * { box-sizing: border-box; margin: 0; padding: 0; }
  html, body { width: 1200px; height: 900px; overflow: hidden; }
  body {
    background: var(--stage);
    display: flex;
    align-items: center;
    justify-content: center;
    gap: 60px;
    font-family: "Open Sans", sans-serif;
  }
  .card {
    position: relative;
    width: 500px;
    height: 300px;
    border-radius: 22px;
    overflow: hidden;
  }
  /* Back: contact side */
  .card-back { background: var(--navy); }
  .back-mark {
    position: absolute;
    left: 20px; top: 0;
    width: 230px; height: 300px;
    display: flex; align-items: center; justify-content: center;
  }
  .back-mark .mark-name {
    font-family: "Cinzel", serif;
    font-weight: 700;
    font-size: 24px;
    letter-spacing: 1.5px;
    color: var(--white);
    white-space: nowrap;
  }
  .divider {
    position: absolute;
    left: 262px; top: 40px;
    width: 1px; height: 220px;
    background: linear-gradient(to bottom, transparent, rgba(140,160,200,.55), transparent);
  }
  .contact {
    position: absolute;
    left: 290px; top: 92px;
    color: var(--text-light);
    font-size: 12.5px;
    line-height: 1.45;
  }
  .contact .person {
    font-family: "Cinzel", serif;
    font-weight: 700;
    font-size: 16px;
    color: var(--accent-blue);
    letter-spacing: .5px;
  }
  .contact .title { margin-bottom: 4px; }
  .contact .licence-label { color: var(--accent-blue); }
  .contact ul { list-style: none; margin-top: 4px; }
  .contact li { display: flex; align-items: center; gap: 7px; }
  .contact svg { width: 10px; height: 10px; fill: var(--accent-blue); flex: none; }

  /* Front: brand side */
  .card-front { color: var(--white); }
  .water {
    position: absolute; inset: 0;
    background:
      radial-gradient(ellipse at 70% 40%, rgba(150,200,245,.45), transparent 60%),
      linear-gradient(160deg, var(--water-mid), var(--water-deep) 55%, var(--water-light));
  }
  .brand {
    position: absolute;
    left: 150px; top: 110px;
  }
  .brand-name {
    font-family: "Cinzel", serif;
    font-weight: 700;
  }
  .brand-name .primary { display: block; font-size: 27px; letter-spacing: 1.5px; line-height: 1; }
  .brand-name .secondary {
    display: block; font-size: 11.5px; letter-spacing: 1.6px;
    border-bottom: 1.5px solid var(--white);
    padding: 3px 0 3px;
  }
  .scope {
    position: absolute;
    right: 70px; top: 200px;
    font-weight: 700; font-size: 13px; letter-spacing: .4px;
  }
</style>
</head>
<body>
  <section class="card card-back" aria-label="Business card back">
    <div class="back-mark">
      <span class="mark-name">AZURE HAVEN</span>
    </div>
    <div class="divider"></div>
    <div class="contact">
      <p class="person">DANIEL VOSS</p>
      <p class="title">President</p>
      <p><span class="licence-label">LICENCE NO:</span> CPC 1234567</p>
      <ul>
        <li><svg viewBox="0 0 10 10"><path d="M2 1h2l1 2-1 1a5 5 0 0 0 2 2l1-1 2 1v2c0 .6-.4 1-1 1A8 8 0 0 1 1 2c0-.6.4-1 1-1z"/></svg>904-555-0147</li>
        <li><svg viewBox="0 0 10 10"><path d="M0 2h10v6H0zM1 3l4 3 4-3"/></svg>hello@azurehavenfl.com</li>
        <li><svg viewBox="0 0 10 10"><circle cx="5" cy="5" r="4.5"/></svg>azurehavenfl.com</li>
      </ul>
    </div>
  </section>

  <section class="card card-front" aria-label="Business card front">
    <div class="water" role="img" aria-label="Rippling blue pool water photograph"></div>
    <div class="brand">
      <p class="brand-name">
        <span class="primary">AZURE HAVEN</span>
        <span class="secondary">OF NORTHEAST FLORIDA</span>
      </p>
    </div>
    <p class="scope">REMODEL | REPAIR | SERVICE</p>
  </section>
</body>
</html>
```